Kaffeerösterei sucht Etiketten-Design
- schnelle Ausführung - mein Geschmack voll getroffen - unkompliziert und Kunden orientiert bei der Ausführung
Zielgruppe
Kaffeerösterei für die edelsten und teuersten Rohkaffees.
Meine Kunden sind Kaffee Geniesser.
Aufgabenstellung
Transparente Aufkleber für eine Schiefertafel im Format 22.5 cm x 15.5 cm.
Im Hand-Lettering Stil.
5 Schiefertafeln sind gewünscht.
Tafel 1
Kostenlos zur Degustation
Espresso
Café Crème 3.--
Americano 3.--
Filter Kaffee 3.--
Tafel 2
Kaffee & Milch
Cappuccino 4.--
Café Latte 4.--
Flat White 4.--
Latte Macchiato 4.--
Latte Macchiato mit Aroma 5.--
Kaffee & Hafermilch + 1.--
Tafel 3
Crepes
Pikant
- Pizza Crepes 7.--
- Flammkuchen Crepes 7.--
Süss
- Schoggi Crepes 6.--
- Apfelmus & Zimtzucker 6.--
Tafel 4
Kaffee & Schnaps
- Original Entlebucher Schwarzes 7.--
- Espresso Coretto 5.00
- Schwarzes mit Rahmhaube 8.--
Tafel 5
Schokolade & Milch
- heisse Schoggi 5.--
- heisse Schoggi mit Rahmhaube 6.--
- heisse Schoggi mit Espresso 6.--
- Schokolade & Hafermilch +1.--
Als Idee, was mir gefallen könnte:
https://www.bildsammlung.example/pin/104857392018374655/
https://de.grafikhort.example/vektorkunst/4418203-set-kaffeekarte-mit-tassen-kaffeegetranken-im-vintage-stil-stilisierte-zeichnung-mit-kreide-auf-tafel-schriftzug-sample-drinks
https://www.fotolager.example/stockfoto-heisser-kakao-bar-warm-hier-oben-hand-tafel-caf-schild-an-tafel-hintergrund-mit-farbe-kreide-schriftzug-werbung-fur-heisse-d-583021746.html

```html
<!DOCTYPE html>
<html lang="de">
<head>
<meta charset="utf-8">
<title>Kaffee &amp; Milch – Tafel 2</title>
<link rel="stylesheet" href="https://fonts.googleapis.com/css2?family=Amatic+SC:wght@700&family=Caveat+Brush&display=swap">
<style>
  :root {
    --paper: #ffffff;
    --slate: #1d1d1b;
    --chalk: #ffffff;
  }
  * { margin: 0; padding: 0; box-sizing: border-box; }
  html, body {
    width: 1200px;
    height: 856px;
    overflow: hidden;
    background: var(--paper);
  }
  .sticker {
    position: absolute;
    left: 62px;
    top: 62px;
    width: 1075px;
    height: 733px;
    background: var(--slate);
    color: var(--chalk);
  }
  .title {
    position: absolute;
    left: 0;
    right: 0;
    top: 48px;
    text-align: center;
    font-family: "Caveat Brush", cursive;
    font-size: 104px;
    line-height: 1;
    font-weight: 400;
  }
  .flourish {
    position: absolute;
    top: 98px;
    width: 76px;
    height: 30px;
    border-radius: 15px;
    background: linear-gradient(90deg, rgba(255,255,255,0.15), rgba(255,255,255,0.55), rgba(255,255,255,0.15));
  }
  .flourish--left { left: 119px; }
  .flourish--right { left: 887px; }
  .menu {
    position: absolute;
    top: 210px;
    left: 0;
    list-style: none;
  }
  .menu-item {
    display: flex;
    align-items: baseline;
    height: 80.2px;
  }
  .menu-item__name {
    width: 731px;
    text-align: right;
    font-family: "Amatic SC", cursive;
    font-weight: 700;
    font-size: 74px;
    line-height: 80px;
    letter-spacing: 1px;
    white-space: nowrap;
  }
  .menu-item__note {
    font-size: 32px;
    letter-spacing: 0.5px;
  }
  .menu-item__price {
    width: 185px;
    text-align: right;
    font-family: "Caveat Brush", cursive;
    font-size: 78px;
    line-height: 80px;
    white-space: nowrap;
  }
</style>
</head>
<body>
  <main class="sticker">
    <span class="flourish flourish--left" role="img" aria-label="Geschwungene Zierlinie links"></span>
    <h1 class="title">Kaffee &amp; Milch</h1>
    <span class="flourish flourish--right" role="img" aria-label="Geschwungene Zierlinie rechts"></span>
    <ul class="menu">
      <li class="menu-item"><span class="menu-item__name">Cappuccino</span><span class="menu-item__price">4,–</span></li>
      <li class="menu-item"><span class="menu-item__name">Café Latte</span><span class="menu-item__price">4,–</span></li>
      <li class="menu-item"><span class="menu-item__name">Flat White</span><span class="menu-item__price">4,–</span></li>
      <li class="menu-item"><span class="menu-item__name">Latte Macchiato</span><span class="menu-item__price">4,–</span></li>
      <li class="menu-item"><span class="menu-item__name">Latte Macchiato <span class="menu-item__note">mit Aroma</span></span><span class="menu-item__price">5,–</span></li>
      <li class="menu-item"><span class="menu-item__name">Kaffee &amp; Hafermilch</span><span class="menu-item__price">+1,–</span></li>
    </ul>
  </main>
</body>
</html>
```